Resturant needs packaging design for cones "take away"

We need a design for the packaging of "take-away cones". we serve fries or shrimps in the salted cones. attached are 2 pictures for reference. currently we are using 2 plastic cups to cover both sides of the cone and stickers to attach them to each other.

our requirements are:
- cost effective in terms of materials for production (preferably cardboard or transperant)
- moderately traps heat (covered from both sides), like a box
- not time consuming during order dispatch

Requirements
Should not have
• pictures & bold designs. needs to be simple

```html
<!DOCTYPE html>
<html lang="en">
<head>
<meta charset="utf-8">
<title>Take-away cone packaging dieline</title>
<link rel="stylesheet" href="https://fonts.googleapis.com/css2?family=Arimo:wght@400&display=swap">
<style>
  :root {
    --paper: #fdfdfd;
    --cone-red: #e31e24;
    --cone-yellow: #ffed00;
    --glue-tab: #e9ebeb;
    --badge-dark: #2d2a26;
    --badge-text: #ffffff;
  }
  html, body {
    margin: 0;
    padding: 0;
    width: 1200px;
    height: 1084px;
    overflow: hidden;
    background: var(--paper);
  }
  .dieline {
    display: block;
    width: 1200px;
    height: 1084px;
  }
  .glue-tab { fill: var(--glue-tab); }
  .panel-red { fill: var(--cone-red); }
  .lid-red { fill: var(--cone-red); }
  .lid-notch { fill: var(--paper); }
  .badge-disc { fill: var(--badge-dark); }
  .badge-label {
    font-family: "Arimo", Arial, sans-serif;
    font-weight: 400;
    font-size: 62px;
    fill: var(--badge-text);
  }
</style>
</head>
<body>
<svg class="dieline" viewBox="0 0 1474 1330" xmlns="http://www.w3.org/2000/svg" aria-label="Cone packaging dieline with lid">
  <defs>
    <linearGradient id="fade-top" x1="0" y1="0" x2="0" y2="1">
      <stop offset="0" stop-color="#ffffff"/>
      <stop offset="0.35" stop-color="#ffffff"/>
      <stop offset="0.85" stop-color="#ffed00"/>
      <stop offset="1" stop-color="#ffed00"/>
    </linearGradient>
    <linearGradient id="fade-left" x1="0.2" y1="0" x2="0.6" y2="0.45">
      <stop offset="0" stop-color="#ffffff"/>
      <stop offset="1" stop-color="#ffed00"/>
    </linearGradient>
    <linearGradient id="fade-mid" x1="0.7" y1="0" x2="0.4" y2="0.45">
      <stop offset="0" stop-color="#ffffff"/>
      <stop offset="1" stop-color="#ffed00"/>
    </linearGradient>
    <linearGradient id="fade-right" x1="1" y1="0.15" x2="0.55" y2="0.5">
      <stop offset="0" stop-color="#ffffff"/>
      <stop offset="1" stop-color="#ffed00"/>
    </linearGradient>
  </defs>

  <g class="glue-tabs">
    <polygon class="glue-tab" points="340,383 312,345 378,218 400,211 433,218"/>
    <polygon class="glue-tab" points="631,218 665,211 688,218 752,335 725,385"/>
    <polygon class="glue-tab" points="252,614 250,565 410,515 437,553"/>
    <polygon class="glue-tab" points="631,553 655,515 818,565 816,612"/>
    <polygon class="glue-tab" points="95,723 76,755 430,1125 537,1178"/>
  </g>

  <g class="cone-top-flap">
    <polygon fill="url(#fade-top)" points="437,553 631,553 725,385 631,218 433,218 340,383"/>
  </g>

  <g class="cone-panels">
    <polygon class="panel-red" points="95,723 252,614 537,1178"/>
    <polygon fill="url(#fade-left)" points="252,614 437,553 537,1178"/>
    <polygon class="panel-red" points="437,553 631,553 537,1178"/>
    <polygon fill="url(#fade-mid)" points="631,553 816,612 537,1178"/>
    <polygon class="panel-red" points="816,612 976,723 537,1178"/>
    <polygon fill="url(#fade-right)" points="976,723 1090,873 541,1178"/>
  </g>

  <g class="lid">
    <polygon class="lid-red" points="978,723 1050,545 1240,520 1355,668 1285,848 1090,873"/>
    <circle class="lid-notch" cx="1020" cy="636" r="21"/>
    <circle class="lid-notch" cx="1317" cy="758" r="21"/>
    <ellipse class="badge-disc" cx="1167" cy="696" rx="100" ry="94"/>
    <text class="badge-label" x="1173" y="725" text-anchor="middle">logo</text>
  </g>
</svg>
</body>
</html>
```